Wix web design for healthcare IT consulting firm.

I am looking for a web design built in Wix that it will be easy for me to add or edit content in the future. The web site does not need to be overly complicated, but it should look very polished and professional. I also want to ensure it is mobile device friendly. I do not need any type of on-line purchasing ability. I will eventually do blogs, but for now it is a fairly standard web site with main page, about us, services provided, etc. I would also like a place for potential customers to contact us directly from the web site. I have included a Word document with some content for the web design. I have also included my logo and business card for reference. I would like to utilize similar colors as my business card. One of my primary competitors is https://vontalmhc.example/

Target Market(s)

Target market could be nursing home CEO, CIO, or other leader at an organization that manages long term care facilities.

Number of Pages Required

5+ page

Colors
876aae

Requirements
Must have
• Be designed to be used in Wix. Use the content I provided to create and make web design. Allow to be viewed on mobile device. Please use similar color structure as attached business card. Please use attached logo in design.

```html
<!DOCTYPE html>
<html lang="en">
<head>
<meta charset="utf-8">
<title>BrightPath Healthcare Solutions – Contact Us</title>
<link href="https://fonts.googleapis.com/css2?family=Open+Sans:wght@300;400;600&family=Arimo:wght@400;700&display=swap" rel="stylesheet">
<style>
  :root{
    --purple:#876aae;
    --purple-dark:#5f4590;
    --hero-top:#9a82c0;
    --hero-bottom:#7a5fa6;
    --page:#f4f8fb;
    --field-border:#b9b9c0;
    --placeholder:#9a9aa0;
    --ink:#1e1e22;
    --muted:#a5a5aa;
    --footer:#222222;
    --footer-line:#333333;
    --white:#ffffff;
  }
  *{margin:0;padding:0;box-sizing:border-box}
  html,body{width:997px;height:1200px;overflow:hidden}
  body{position:relative;background:var(--page);font-family:"Open Sans",sans-serif;color:var(--ink)}

  .hero{position:absolute;left:0;top:0;width:997px;height:276px;
    background:linear-gradient(180deg,var(--hero-top),var(--hero-bottom))}
  .site-header{position:absolute;left:0;top:0;width:997px;height:68px;background:rgba(250,248,253,.93)}
  .brand{position:absolute;left:182px;top:19px;display:flex;align-items:center;gap:6px;
    font-family:"Arimo",sans-serif;font-weight:700;font-size:17px;color:var(--purple)}
  .brand-square{width:12px;height:12px;background:var(--purple)}
  .main-nav a{position:absolute;top:31px;font-family:"Arimo",sans-serif;font-size:8px;color:var(--purple-dark);text-decoration:none}
  .hero-title{position:absolute;left:0;width:997px;top:212px;text-align:center;color:var(--white);font-weight:600;font-size:23px}

  .map{position:absolute;left:0;top:276px;width:997px;height:215px;
    background:linear-gradient(135deg,#e9e4d6 0%,#efe3c8 45%,#e6e6e2 100%)}

  .section-title{position:absolute;left:0;width:997px;top:544px;text-align:center;font-weight:300;font-size:20px}
  .field{position:absolute;height:33px;border:1px solid var(--field-border);background:transparent;
    font-size:10px;color:var(--placeholder);padding:9px 7px}
  .field.textarea{height:166px}

  .info{position:absolute;top:988px;display:flex;gap:10px;align-items:flex-start}
  .info svg{margin-top:6px}
  .info-label{font-size:7px;color:var(--muted)}
  .info-value{font-size:11px;color:var(--ink);margin-top:4px}

  .site-footer{position:absolute;left:0;top:1078px;width:997px;height:122px;background:var(--footer)}
  .footer-nav a{position:absolute;top:27px;font-family:"Arimo",sans-serif;font-size:9px;color:var(--white);text-decoration:none}
  .social{position:absolute;top:56px;width:17px;height:17px;background:var(--purple);border-radius:2px}
  .footer-rule{position:absolute;left:0;top:92px;width:997px;height:1px;background:var(--footer-line)}
  .copyright{position:absolute;left:0;width:997px;top:102px;text-align:center;font-size:7px;color:#8a8a8e}
</style>
</head>
<body>
  <section class="hero" role="img" aria-label="Photo of a modern office reception with people walking, under a purple tint"></section>
  <header class="site-header">
    <div class="brand"><span class="brand-square"></span>BrightPath</div>
    <nav class="main-nav">
      <a style="left:533px" href="#">Home</a>
      <a style="left:584px" href="#">About Us</a>
      <a style="left:645px" href="#">Services Provided</a>
      <a style="left:736px" href="#">Blog</a>
      <a style="left:776px" href="#">Contact Us</a>
    </nav>
  </header>
  <h1 class="hero-title">CONTACT US</h1>

  <div class="map" role="img" aria-label="Street map showing the office location"></div>

  <h2 class="section-title">Contact Us</h2>
  <div class="field" style="left:295px;top:608px;width:195px">Select doctor</div>
  <div class="field" style="left:506px;top:608px;width:196px">Select Time</div>
  <div class="field" style="left:295px;top:655px;width:195px">Your Name</div>
  <div class="field" style="left:506px;top:655px;width:196px">Phone</div>
  <div class="field" style="left:295px;top:704px;width:195px">Your Email</div>
  <div class="field" style="left:506px;top:704px;width:196px">11/11/1111</div>
  <div class="field textarea" style="left:295px;top:751px;width:406px">Your Message*</div>

  <div class="info" style="left:220px">
    <svg width="12" height="18" viewBox="0 0 12 18" fill="none" stroke="#876aae" stroke-width="1.3"><rect x="1" y="1" width="10" height="16" rx="2"/><line x1="5" y1="14.5" x2="7" y2="14.5"/></svg>
    <div><div class="info-label">Give us a Call</div><div class="info-value">555-014-2290</div></div>
  </div>
  <div class="info" style="left:428px">
    <svg width="18" height="13" viewBox="0 0 18 13" fill="none" stroke="#876aae" stroke-width="1.3"><rect x="1" y="1" width="16" height="11" rx="1"/><path d="M1 1.5l8 6 8-6"/></svg>
    <div><div class="info-label">Send us a Message</div><div class="info-value">mlee@brightpathhcs.example</div></div>
  </div>
  <div class="info" style="left:640px">
    <svg width="14" height="18" viewBox="0 0 14 18" fill="none" stroke="#876aae" stroke-width="1.3"><path d="M7 17s6-6 6-10A6 6 0 0 0 1 7c0 4 6 10 6 10z"/><circle cx="7" cy="7" r="2"/></svg>
    <div><div class="info-label">Visit our Location</div><div class="info-value">------------------------------</div></div>
  </div>

  <footer class="site-footer">
    <nav class="footer-nav">
      <a style="left:339px" href="#">Home</a>
      <a style="left:397px" href="#">About Us</a>
      <a style="left:468px" href="#">Services Provided</a>
      <a style="left:572px" href="#">Blog</a>
      <a style="left:618px" href="#">Contact Us</a>
    </nav>
    <span class="social" style="left:415px"></span>
    <span class="social" style="left:453px"></span>
    <span class="social" style="left:492px"></span>
    <span class="social" style="left:531px"></span>
    <span class="social" style="left:569px"></span>
    <div class="footer-rule"></div>
    <p class="copyright">BRIGHTPATH HEALTHCARE &nbsp; 2019 / All Rights Reserved</p>
  </footer>
</body>
</html>
```